Criação de Papelaria (6 itens) para Arquitetura
" Está sendo concluída a fábrica dos revestimentos, que será a responsável pela produção de todos os produtos 3D: painéis, murais, cobogós e imitações em pedra, em sua maioria fabricados em gesso especial, exclusivo da Ventra Relevo "

```html
<!DOCTYPE html>
<html lang="pt-BR">
<head>
<meta charset="UTF-8">
<title>Ventra Relevo — Papel Timbrado</title>
<link rel="stylesheet" href="https://fonts.googleapis.com/css2?family=Montserrat:wght@400;600&display=swap">
<style>
  :root {
    --backdrop: #d9dbde;
    --paper: #ffffff;
    --navy: #1b2a5c;
    --teal: #2fa89a;
    --ink: #3a4150;
    --rule: #1b2a5c;
  }
  * { margin: 0; padding: 0; box-sizing: border-box; }
  html, body {
    width: 1200px;
    height: 1200px;
    overflow: hidden;
    background: var(--backdrop);
    font-family: "Montserrat", Arial, sans-serif;
  }
  .canvas {
    width: 1200px;
    height: 1200px;
    display: flex;
    align-items: center;
    justify-content: center;
  }
  .letterhead {
    position: relative;
    width: 778px;
    height: 1100px;
    background: var(--paper);
    box-shadow: 0 6px 24px rgba(0, 0, 0, 0.12);
    overflow: hidden;
  }
  .letterhead__header {
    position: absolute;
    top: 48px;
    left: 0;
    right: 0;
    display: flex;
    align-items: center;
    gap: 18px;
    padding: 0 0;
  }
  .header-rule {
    flex: 1;
    height: 2px;
    background: var(--rule);
  }
  .brand {
    display: flex;
    align-items: center;
    gap: 10px;
  }
  .brand__dot {
    width: 14px;
    height: 14px;
    border-radius: 50%;
    background: var(--navy);
  }
  .brand__name {
    font-weight: 600;
    font-size: 22px;
    letter-spacing: 1px;
    color: var(--navy);
  }
  .letterhead__footer {
    position: absolute;
    left: 0;
    right: 0;
    bottom: 44px;
    display: flex;
    justify-content: space-between;
    align-items: center;
    padding: 0 64px;
  }
  .contact {
    display: flex;
    align-items: center;
    gap: 10px;
    font-size: 11px;
    line-height: 1.45;
    color: var(--ink);
  }
  .contact__icon {
    width: 22px;
    height: 22px;
    flex-shrink: 0;
  }
  .letterhead__band {
    position: absolute;
    left: 0;
    right: 0;
    bottom: 0;
    height: 18px;
    background: var(--navy);
    border-top: 4px solid var(--teal);
  }
</style>
</head>
<body>
<main class="canvas">
  <article class="letterhead">
    <header class="letterhead__header">
      <span class="header-rule"></span>
      <div class="brand">
        <span class="brand__dot"></span>
        <span class="brand__name">Ventra Relevo</span>
      </div>
      <span class="header-rule"></span>
    </header>

    <footer class="letterhead__footer">
      <div class="contact contact--phone">
        <svg class="contact__icon" viewBox="0 0 22 22" aria-hidden="true">
          <circle cx="11" cy="11" r="11" fill="#1b2a5c"/>
          <path d="M8 6.5l1.6 2.3-1 1.1c.6 1.3 1.6 2.3 2.9 2.9l1.1-1 2.3 1.6-.7 1.6c-3.8-.3-6.7-3.2-7-7z" fill="#fff"/>
        </svg>
        <span>(11) 3480-2217<br>(11) 98812-5530</span>
      </div>
      <div class="contact contact--web">
        <svg class="contact__icon" viewBox="0 0 22 22" aria-hidden="true">
          <circle cx="11" cy="11" r="11" fill="#1b2a5c"/>
          <circle cx="11" cy="11" r="5.5" fill="none" stroke="#fff" stroke-width="1.2"/>
          <path d="M5.5 11h11M11 5.5c-2 2.8-2 8.2 0 11M11 5.5c2 2.8 2 8.2 0 11" fill="none" stroke="#fff" stroke-width="1"/>
        </svg>
        <span>www.ventrarelevo.com.br</span>
      </div>
      <div class="contact contact--address">
        <svg class="contact__icon" viewBox="0 0 22 22" aria-hidden="true">
          <circle cx="11" cy="11" r="11" fill="#1b2a5c"/>
          <path d="M11 5.5a3.6 3.6 0 0 0-3.6 3.6c0 2.7 3.6 7 3.6 7s3.6-4.3 3.6-7A3.6 3.6 0 0 0 11 5.5z" fill="#fff"/>
          <circle cx="11" cy="9.1" r="1.3" fill="#1b2a5c"/>
        </svg>
        <span>Rua das Acácias, 240<br>Jundiaí - SP</span>
      </div>
    </footer>

    <div class="letterhead__band"></div>
  </article>
</main>
</body>
</html>
```